Payroll Brochure

Create a brochure with the copy i have provided . A simple easy tp read brochure that shows wat we do we handle payroll taxes insurance 401k etc

```html
<!DOCTYPE html>
<html lang="en">
<head>
<meta charset="utf-8">
<title>Orvale Payroll Brochure</title>
<link rel="stylesheet" href="https://fonts.googleapis.com/css2?family=Libre+Baskerville:wght@400;700&family=Lato:wght@400;700&display=swap">
<style>
  :root {
    --gold: #c89b45;
    --gold-light: #e6c577;
    --maroon: #6b0f12;
    --brown: #8e4b22;
    --ink: #2b2b2b;
    --page: #ffffff;
    --stage: #252525;
    --serif: "Libre Baskerville", Georgia, serif;
    --sans: "Lato", Arial, sans-serif;
  }
  * { box-sizing: border-box; margin: 0; padding: 0; }
  html, body { width: 900px; height: 1200px; overflow: hidden; background: var(--stage); }
  .canvas { position: relative; width: 900px; height: 1200px; font-family: var(--sans); color: var(--ink); }
  .spread { position: absolute; left: 76px; width: 728px; height: 513px; overflow: hidden; background: var(--page); }
  .spread--outer { top: 80px; }
  .spread--inner { top: 626px; background: linear-gradient(90deg, #f4f4f4 0%, #e9e9e9 48%, #fafafa 52%, #f2f2f2 100%); }
  .abs { position: absolute; }
  .fold-shade { position: absolute; left: 352px; top: 0; width: 30px; height: 100%; background: linear-gradient(90deg, rgba(0,0,0,0) 0%, rgba(0,0,0,.06) 45%, rgba(0,0,0,0) 100%); pointer-events: none; }

  /* outer spread */
  .crowd-fade { position: absolute; left: 0; top: 320px; width: 728px; height: 170px; background: linear-gradient(180deg, rgba(230,230,230,0) 0%, rgba(225,225,225,.55) 60%, rgba(235,235,235,.3) 100%); }
  .qual-title { left: 32px; top: 42px; font-family: var(--serif); color: var(--gold); line-height: 1; }
  .qual-title .l1 { font-size: 25px; }
  .qual-title .l2 { font-size: 19px; margin-top: 6px; color: var(--maroon); }
  .qual-title .l3 { font-size: 10.5px; font-weight: 700; margin-top: 7px; }
  .qual-title b { color: var(--maroon); font-weight: 700; }
  .qual-title .gold { color: var(--gold); }
  .feature { left: 32px; width: 298px; font-size: 7.2px; line-height: 1.5; }
  .tag { display: inline-block; color: #fff; font-size: 7.2px; padding: 1px 4px; margin-right: 4px; text-transform: uppercase; line-height: 1.2; }
  .tag--maroon { background: var(--maroon); }
  .tag--brown { background: var(--brown); }
  .rule { left: 32px; width: 168px; height: 2px; background: var(--brown); }
  .contact { left: 60px; top: 368px; width: 266px; text-align: center; }
  .contact h2 { font-family: var(--serif); font-size: 20px; color: var(--maroon); font-weight: 700; }
  .contact h2 span { color: var(--gold); }
  .contact .line { width: 150px; height: 1.5px; background: var(--gold); margin: 5px auto 6px; }
  .contact .phone { font-family: var(--serif); font-size: 23px; color: #111; }
  .contact .web { font-size: 9.5px; letter-spacing: 2.5px; margin-top: 2px; }
  .advantage { left: 394px; top: 372px; font-family: var(--serif); color: #111; line-height: 1; }
  .advantage .the { font-size: 27px; }
  .advantage .the b { color: var(--maroon); font-size: 32px; }
  .advantage .big { font-size: 34px; margin-top: 2px; }
  .advantage .sub { font-family: var(--sans); font-size: 5.6px; margin-top: 10px; margin-left: 6px; }
  .brand { position: absolute; left: 445px; top: 62px; width: 200px; text-align: center; font-family: var(--serif); font-size: 30px; font-weight: 700; color: var(--maroon); line-height: 1; }
  .brand i { display: inline-block; width: 22px; height: 22px; background: var(--gold); margin-right: 8px; vertical-align: -1px; }
  .band-web { right: 90px; top: 492px; color: #fff; font-size: 9.5px; letter-spacing: 2.5px; }

  /* inner spread */
  .sec-title { font-family: var(--serif); font-weight: 700; line-height: 1; }
  .payroll-title { left: 22px; top: 36px; font-size: 20px; color: var(--maroon); }
  .payroll-title span { color: var(--gold); }
  .copy { font-size: 7px; line-height: 1.5; }
  .copy p + p { margin-top: 7px; }
  .copy b { font-weight: 700; }
  .tax-box { left: 14px; top: 186px; width: 344px; background: var(--maroon); color: #fff; padding: 14px 14px 10px; }
  .tax-label { left: 68px; top: 174px; width: 232px; height: 21px; background: var(--gold); text-align: center; font-family: var(--serif); font-size: 13px; line-height: 21px; color: #3a0a0a; z-index: 2; }
  .photo { position: absolute; }
  .list-line { left: 152px; top: 286px; width: 2px; height: 158px; background: var(--gold); }
  .dot { left: 148px; width: 9px; height: 9px; border-radius: 50%; background: var(--maroon); }
  .list-item { left: 172px; width: 180px; }
  .benefit-title { left: 364px; width: 364px; top: 36px; text-align: center; font-size: 18px; color: var(--maroon); }
  .app-title { left: 380px; top: 258px; width: 126px; text-align: center; font-family: var(--serif); font-size: 13px; line-height: 1.2; }
  .app-title .a { color: var(--gold); font-weight: 700; }
  .app-title .b { color: var(--maroon); }
  .app-copy { left: 386px; top: 300px; width: 136px; text-align: justify; }
  .onboard-label { left: 545px; top: 172px; width: 154px; height: 21px; background: var(--maroon); color: #fff; text-align: center; font-family: var(--serif); font-size: 13px; line-height: 21px; z-index: 2; }
  .onboard-box { left: 534px; top: 186px; width: 176px; background: linear-gradient(180deg, #d8a93d, #c99426); padding: 14px 10px 10px; color: #fff; font-size: 6.8px; line-height: 1.45; }
  .onboard-box p + p { margin-top: 11px; }
</style>
</head>
<body>
<div class="canvas">

  <!-- Outer spread: back cover and front cover -->
  <section class="spread spread--outer">
    <div class="crowd-fade" role="img" aria-label="Faint crowd of cheering people in silhouette"></div>

    <svg class="abs" style="left:0;top:0" width="728" height="513" viewBox="0 0 728 513" aria-hidden="true">
      <defs>
        <linearGradient id="goldDiamond" x1="0" y1="0" x2="1" y2="1">
          <stop offset="0" stop-color="#f0d58d"/>
          <stop offset=".5" stop-color="#c99a45"/>
          <stop offset="1" stop-color="#a9742d"/>
        </linearGradient>
        <linearGradient id="bandGrad" x1="0" y1="0" x2="1" y2="0">
          <stop offset="0" stop-color="#e2bf63"/>
          <stop offset=".45" stop-color="#c9963f"/>
          <stop offset="1" stop-color="#8e4b22"/>
        </linearGradient>
        <linearGradient id="brownGrad" x1="0" y1="0" x2="1" y2="1">
          <stop offset="0" stop-color="#a5592a"/>
          <stop offset="1" stop-color="#6e3517"/>
        </linearGradient>
      </defs>
      <polygon points="620,15 700,45 700,330 640,270" fill="url(#brownGrad)"/>
      <polygon points="300,190 470,0 580,0 405,195 560,360 500,360" fill="url(#goldDiamond)" opacity=".85"/>
      <polygon points="320,190 485,10 500,10 340,190 500,355 485,355" fill="#f3dc9c" opacity=".9"/>
      <polygon points="470,250 600,120 728,250 600,380" fill="url(#goldDiamond)"/>
      <polygon points="560,300 640,225 720,300 640,375" fill="#e8c96f" opacity=".7"/>
      <circle cx="545" cy="180" r="152" fill="#fff"/>
      <circle cx="545" cy="180" r="148" fill="none" stroke="#6b0f12" stroke-width="7"/>
      <path d="M0 485 H640 L668 513 H0 Z" fill="url(#bandGrad)"/>
      <path d="M640 485 H700 L728 513 H668 Z" fill="#8e4b22"/>
    </svg>

    <div class="photo" style="left:401px;top:36px;width:288px;height:288px;border-radius:50%;clip-path:inset(88px 0 0 0);background:linear-gradient(180deg,#eef0f2 30%,#d9c9bf 60%,#6d6a73 100%);" role="img" aria-label="Group photo of smiling office staff standing together"></div>
    <div class="brand"><i></i>Orvale</div>

    <div class="abs qual-title">
      <div class="l1">WHAT MAKES <b>ORVALE</b></div>
      <div class="l2">UNIQUELY <span class="gold">QUALIFIED</span></div>
      <div class="l3">TO BE YOUR SERVICE <b>PROVIDER?</b></div>
    </div>

    <p class="abs feature" style="top:133px"><span class="tag tag--maroon">People</span>Orvale has gone to great lengths to hire and train a world-class team of experienced payroll and HR professionals that are genuinely interested in making sure our clients receive the very best in service and support.</p>
    <div class="abs rule" style="top:180px"></div>
    <p class="abs feature" style="top:190px"><span class="tag tag--brown">Process</span>Developed over the years, the Orvale process has been designed with speed and accuracy in mind. Orvale does what's needed to make sure our clients are presented with speedy responses to their questions, and produce accurate, reliable, and timely payrolls. With Orvale's custom designed software, we can easily tailor to your payroll needs.</p>
    <div class="abs rule" style="top:254px"></div>
    <p class="abs feature" style="top:269px"><span class="tag tag--maroon">Products</span>Orvale has developed a comprehensive suite of products and services that will fit your needs.</p>
    <div class="abs rule" style="top:295px"></div>
    <p class="abs feature" style="top:302px"><span class="tag tag--brown">Flexibility</span>Orvale will design HR solutions that meet your specific needs and requirements.</p>

    <div class="abs contact">
      <h2>CONTACT <span>DETAILS</span></h2>
      <div class="line"></div>
      <div class="phone">123 1234 123</div>
      <div class="web">www.yourwebsite.com</div>
    </div>

    <div class="abs advantage">
      <div class="the">THE <b>ORVALE</b></div>
      <div class="big">Advantage</div>
      <div class="sub">developed a comprehensive suite of products and services that will fit your needs.</div>
    </div>

    <div class="abs band-web">www.yourwebsite.com</div>
    <div class="fold-shade"></div>
  </section>

  <!-- Inner spread -->
  <section class="spread spread--inner">
    <svg class="abs" style="left:0;top:0" width="728" height="513" viewBox="0 0 728 513" aria-hidden="true">
      <defs>
        <linearGradient id="bandGrad2" x1="0" y1="0" x2="1" y2="0">
          <stop offset="0" stop-color="#e2bf63"/>
          <stop offset=".5" stop-color="#c9963f"/>
          <stop offset="1" stop-color="#8e4b22"/>
        </linearGradient>
      </defs>
      <path d="M85 480 H728 V513 H55 Z" fill="url(#bandGrad2)"/>
    </svg>

    <h2 class="abs sec-title payroll-title"><span>PAYROLL</span> AND</h2>
    <div class="abs copy" style="left:22px;top:64px;width:330px">
      <p>Flexible – Orvale's flexible and powerful payroll module allows you the ability to grow you're your business by meeting your unique needs. Supporting payrolls for very large to very small companies.</p>
      <p>Efficient – Get payroll done efficiently and accurately by relying on our flexible design to handle even the most complex payroll needs.</p>
      <p>Grow without Growing Pains – Orvale's technology and design is able to allow you to scale your business without adding all the incremental costs typically required.</p>
    </div>

    <div class="abs copy tax-box">
      <p>Accurate – all payroll taxes (federal, state, local) are calculated accurately. Additionally, we determine proper local tax jurisdictions based on the employee home and work addresses.</p>
      <p>Complete – Federal, State, and Local withholding taxes as well as State and Federal Unemployment taxes are provided. Tax payments are integrated into the Accounts Payable and General Ledger modules.</p>
    </div>
    <div class="abs tax-label">TAX REPORTING &amp; PAYMENTS</div>

    <div class="photo" style="left:12px;top:288px;width:144px;height:162px;background:linear-gradient(135deg,#2c2c30 0%,#6a6e78 55%,#d8d8dc 100%);" role="img" aria-label="Hands working on a calculator beside paperwork"></div>
    <div class="abs list-line"></div>
    <div class="abs dot" style="top:292px"></div>
    <div class="abs dot" style="top:347px"></div>
    <div class="abs dot" style="top:397px"></div>
    <div class="abs copy list-item" style="top:288px"><b>COMPLETE</b> -Federal, State, and Local withholding taxes as well as State and Federal Unemployment taxes are provided.Tax payments are integrated into the Accounts Payable and General Ledger modules.</div>
    <div class="abs copy list-item" style="top:343px"><b>GET BIG COMPANY SERVICES –</b> by using our online tools in conjunction with your service team, you will have access to HR services only afforded by some of the largest companies.</div>
    <div class="abs copy list-item" style="top:393px"><b>LIBRARY –</b> our online document library lets you and employees create your own library of information accessible at any time. Employees can upload documents and forms that can be kept in history as long as needed.</div>

    <h2 class="abs sec-title benefit-title">BENEFIT ENROLLMENT</h2>
    <div class="abs copy" style="left:380px;top:62px;width:328px">Easy and Quick Enrollment – <b>our intuitive user experience quickly walks employees through their benefit enrollment process and allows them to compare different plans and select those that best meet their life needs.</b></div>
    <div class="abs copy" style="left:380px;top:110px;width:156px">Easy and Quick Enrollment – <b>our intuitive user experience quickly walks employees through their benefit enrollment process and allows them to compare different plans and select those that best meet their life needs.</b></div>
    <div class="abs copy" style="left:554px;top:110px;width:154px">You Pick – with our flexible contribution setup features, you can contribute in any manner to your employees' benefits while the system automatically processes them through payroll</div>

    <div class="photo" style="left:380px;top:180px;width:126px;height:70px;background:linear-gradient(135deg,#e9d8c8 0%,#b99a82 50%,#5d4a3e 100%);" role="img" aria-label="Close-up of a finger pressing calculator keys"></div>
    <div class="abs app-title"><div class="a">APPLICANT</div><div class="b">TRACKING</div></div>
    <div class="abs copy app-copy">
      <p>Create and Post Jobs – you can create jobs with just a few clicks and post them on all the popular job sites.</p>
      <p>Hire the Right People – by posting on popular job boards, as well as a proprietary database of job seekers, you will reach more candidates. You can choose to receive profiles of candidates that only match your background and specifications.</p>
    </div>

    <div class="abs onboard-box">
      <p>Customize your On Boarding – <b>you can customize your on boarding experience to your hiring needs as well as provide multiple workflows for different employee types. The on boarding experience can be branded for you, providing a personalized experience for the employees.</b></p>
      <p>Custom Document Management – <b>our custom document mapping feature lets you use your own forms and documents as part of the on boarding and hiring process. When these forms are completed – and electronically signed – they stay in history as long as needed.</b></p>
      <p>Intuitive – <b>with a focus on the user experience, your employees will find it easy and quick to get on boarded with you.</b></p>
    </div>
    <div class="abs onboard-label">ON BOARDING</div>

    <div class="abs copy" style="left:380px;top:432px;width:330px">Manage the Hiring Process – review candidates via video or online conferencing, review voice interviews, schedule in person interviews, have candidates answer certain online questions, and manage this entire process to find the right people. Once hired, they can be on boarded automatically.</div>

    <div class="abs band-web" style="top:490px;right:78px">www.yourwebsite.com</div>
    <div class="fold-shade"></div>
  </section>

</div>
</body>
</html>
```